Investment Advisor E-Newsletter Banner Design

I need a banner designed for an email newsletter that will be sent monthly to clients and prospects. We want to see designs that are elegant and use our logo well. The banner should be 922x150px and should go well with the www.bltvorna.com website. Should include Logo and email and phone number.

Target Market(s)

High net worth investors

Number of Pages Required

1 page

Requirements
Must have
• logo, place for email (info@bltvorna.com) and phone number (555-297-6184), colors and design that work well with www.bltvorna.com website

```html
<!DOCTYPE html>
<html lang="en">
<head>
<meta charset="utf-8">
<title>Bltvorna Capital – Newsletter Banner</title>
<link rel="stylesheet" href="https://fonts.googleapis.com/css2?family=Open+Sans:wght@400&display=swap">
<style>
  :root {
    --navy: #27307a;
    --navy-deep: #1d2566;
    --ink: #2c2f7c;
    --paper: #f4f2ee;
    --wood-light: #efebe5;
    --wood-mid: #e4ded5;
    --photo-top: #e6e1da;
    --photo-bottom: #ebe6df;
    --white: #ffffff;
  }
  * { margin: 0; padding: 0; box-sizing: border-box; }
  html, body { width: 1200px; height: 195px; overflow: hidden; background: var(--paper); }
  .banner {
    position: relative;
    width: 1200px;
    height: 195px;
    overflow: hidden;
    background: linear-gradient(90deg, var(--paper) 0%, var(--wood-light) 45%, var(--wood-mid) 100%);
    font-family: "Open Sans", Arial, sans-serif;
  }
  .hero-photo {
    position: absolute;
    left: 530px;
    top: 0;
    width: 230px;
    height: 195px;
    background: linear-gradient(180deg, var(--photo-top) 0%, var(--photo-bottom) 100%);
  }
  .brand {
    position: absolute;
    left: 30px;
    top: 26px;
    display: flex;
    align-items: center;
    gap: 18px;
    color: var(--navy);
  }
  .brand-mark {
    width: 80px;
    height: 80px;
    background: var(--navy);
  }
  .brand-name {
    font-weight: 400;
    line-height: 1.15;
  }
  .brand-name .primary { display: block; font-size: 42px; }
  .brand-name .secondary { display: block; font-size: 22px; padding-left: 2px; }
  .contact {
    position: absolute;
    top: 152px;
    left: 44px;
    display: flex;
    gap: 30px;
    color: var(--ink);
    font-size: 21px;
    line-height: 28px;
  }
  .contact-item { display: flex; align-items: center; gap: 10px; }
  .contact-item svg { width: 24px; height: 24px; fill: var(--ink); }
  .audience {
    position: absolute;
    width: 104px;
    height: 104px;
    display: flex;
    align-items: center;
    justify-content: center;
    text-align: center;
    color: var(--white);
    line-height: 1.2;
  }
  .audience::before {
    content: "";
    position: absolute;
    left: 18px; top: 18px;
    width: 68px; height: 68px;
    border-radius: 10px;
    background: var(--navy-deep);
    transform: rotate(45deg);
    box-shadow: 0 2px 4px rgba(0,0,0,0.18);
  }
  .audience span { position: relative; }
  .audience.large span { font-size: 16px; }
  .audience.small span { font-size: 12px; }
  .private-client { left: 764px; top: 16px; }
  .institutions   { left: 848px; top: 78px; }
  .business       { left: 911px; top: 16px; }
  .catholic       { left: 988px; top: 78px; }
  .socially       { left: 1060px; top: 20px; }
</style>
</head>
<body>
<div class="banner">
  <div class="hero-photo" role="img" aria-label="Photo: hands holding a piggy bank over a wooden table"></div>

  <div class="brand">
    <div class="brand-mark"></div>
    <div class="brand-name">
      <span class="primary">Bltvorna Capital</span>
      <span class="secondary">Wealth Partners, Inc.</span>
    </div>
  </div>

  <div class="contact">
    <div class="contact-item">
      <svg viewBox="0 0 24 24" aria-hidden="true"><path d="M6.6 10.8a15.1 15.1 0 0 0 6.6 6.6l2.2-2.2a1 1 0 0 1 1-.25 11.4 11.4 0 0 0 3.6.57 1 1 0 0 1 1 1V20a1 1 0 0 1-1 1A17 17 0 0 1 3 4a1 1 0 0 1 1-1h3.5a1 1 0 0 1 1 1c0 1.25.2 2.45.57 3.57a1 1 0 0 1-.25 1z"/></svg>
      <span>555-297-6184</span>
    </div>
    <div class="contact-item">
      <svg viewBox="0 0 24 24" aria-hidden="true"><path d="M2 5h20v14H2z M4 7v.4l8 5.3 8-5.3V7z" fill-rule="evenodd"/></svg>
      <span>info@bltvorna.com</span>
    </div>
  </div>

  <div class="audience large private-client"><span>Private<br>Client</span></div>
  <div class="audience small institutions"><span>institutions<br>and<br>fundations</span></div>
  <div class="audience large business"><span>business</span></div>
  <div class="audience small catholic"><span>catholic<br>values<br>investors</span></div>
  <div class="audience small socially"><span>Socially<br>responsible<br>investors</span></div>
</div>
</body>
</html>
```